Real Estate Marketing Postcards need a fresh look, Front & Back

I have a current postcard design (attached) that lacks design quality and too much use of color. I do like the basic color scheme, but I'm open to anything that cleans up the look and incorporates space for the existing text. I'm not opposed to a design with a white background, more white space. The design should be full bleed according to the attached specs. I would like this to be sent over in an Adobe format, something like InDesign.

The company logo will remain the same colors and appearance. The headshot will likely be updated in the coming weeks.

I am attaching a sample of a recent card plus a template from the printer showing the back of the card and location of the address and postage section that must remain blank. I am also including the logo and another logo designed for use with a white (or non blue) background.

(feel free to swap in stock photos of whatever house you want, but the front of the card should incorporate at least one photo of a house.)

Target Market(s)

Home owners.

Industry/Entity Type

Real Estate

Font styles to use
Sans Serif

Colors

Designer to choose colors to be used in the design.

Requirements
Must have
• Company logo, the headshot, the contact info on the back, a photo or photos of a house along with the text "Just Sold" or "Sold" featured on the front of the card.

```html
<!DOCTYPE html>
<html lang="en">
<head>
<meta charset="utf-8">
<title>Just Sold Postcard – Front &amp; Back</title>
<link href="https://fonts.googleapis.com/css2?family=Montserrat:ital,wght@0,400;0,500;0,600;0,700;0,800;1,500;1,600&family=Oswald:wght@400;500&display=swap" rel="stylesheet">
<style>
:root{
  --stage:#e6e6e6;
  --charcoal:#555557;
  --charcoal-dark:#454547;
  --brand-blue:#0d4f8f;
  --lime:#a8c83a;
  --light-grey:#dcdcdc;
  --white:#ffffff;
  --ink:#1e1e1e;
  --photo-sky:#8e93b8;
  --photo-house:#5d6477;
  --photo-lawn:#4e6a3c;
  --headshot:#b9a89a;
}
*{margin:0;padding:0;box-sizing:border-box}
html,body{width:1200px;height:1000px;overflow:hidden}
body{background:var(--stage);position:relative;font-family:"Montserrat",Arial,sans-serif;color:var(--ink)}
.card{position:absolute;background:var(--white);overflow:hidden}

/* FRONT */
.card-front{left:52px;top:27px;width:627px;height:446px}
.front-panel{position:absolute;left:0;top:0;width:228px;height:308px;background:var(--charcoal);color:var(--white);text-align:center;padding-top:52px}
.front-panel-foot{position:absolute;left:0;top:399px;width:228px;height:47px;background:var(--charcoal)}
.accent-line{position:absolute;left:228px;top:0;width:4px;height:446px;background:var(--lime)}
.headline-small{font-size:25px;font-weight:600;line-height:31px;letter-spacing:.5px}
.headline-big{font-size:56px;font-weight:800;line-height:53px;letter-spacing:-1.5px;margin-top:6px}
.headline-by{font-size:25px;font-weight:600;margin-top:6px}
.house-photo{position:absolute;left:233px;top:0;width:394px;height:308px;background:linear-gradient(180deg,var(--photo-sky) 0%,#b3a7c0 30%,var(--photo-house) 55%,var(--photo-lawn) 78%,#7d8496 100%)}
.brand-band{position:absolute;left:0;top:313px;width:627px;height:81px;background:var(--brand-blue);color:var(--white);padding:10px 0 0 30px}
.brand-name{font-size:29.5px;font-weight:700;letter-spacing:0;white-space:nowrap}
.brand-tag{font-size:16px;font-style:italic;font-weight:500;margin:3px 0 0 136px}
.front-headshot{position:absolute;left:453px;top:278px;width:146px;height:146px;border:4px solid var(--white);background:var(--headshot)}

/* BACK */
.card-back{left:501px;top:505px;width:626px;height:446px}
.intro{position:absolute;left:0;top:0;width:626px;height:173px;background:var(--light-grey)}
.selling-bar{position:absolute;left:0;top:23px;width:626px;height:47px;background:var(--brand-blue);color:var(--white);display:flex;align-items:center;padding-left:29px}
.selling-title{font-size:45px;font-weight:700;letter-spacing:.8px;line-height:1}
.selling-sub{font-size:17px;font-weight:500;line-height:19px;margin-left:26px}
.intro-copy{position:absolute;left:30px;top:78px;width:560px;font-size:12.6px;line-height:16px}
.intro-cta{position:absolute;left:29px;top:148px;font-size:14.5px;font-weight:600;font-style:italic;color:var(--brand-blue)}
.contact-band{position:absolute;left:0;top:173px;width:626px;height:140px;background:var(--charcoal-dark);color:var(--white)}
.logo-block{position:absolute;left:27px;top:10px;width:110px;height:80px;background:var(--brand-blue);text-align:center;padding-top:24px}
.logo-name{font-size:17px;font-weight:600;line-height:1}
.logo-phone{font-size:12.5px;font-weight:600;margin-top:14px}
.badges{position:absolute;left:27px;top:101px;display:flex;gap:8px}
.badge{width:22px;height:22px;background:var(--white)}
.reasons{position:absolute;left:147px;top:11px;width:152px;font-size:10.2px;font-style:italic;line-height:12.3px;text-align:justify}
.reasons p+p{margin-top:11px}
.divider{position:absolute;left:310px;top:20px;width:1px;height:100px;background:#8a8a8a}
.back-headshot{position:absolute;left:323px;top:15px;width:106px;height:108px;background:var(--headshot)}
.agent{position:absolute;left:438px;top:13px;font-size:12.3px;line-height:14.5px}
.agent-name{font-family:"Oswald","Arial Narrow",sans-serif;font-size:21px;line-height:24px;margin-bottom:3px}
</style>
</head>
<body>

<section class="card card-front" aria-label="Postcard front">
  <div class="front-panel">
    <div class="headline-small">ANOTHER<br>HOME</div>
    <div class="headline-big">JUST<br>SOLD</div>
    <div class="headline-by">BY</div>
  </div>
  <div class="front-panel-foot"></div>
  <div class="accent-line"></div>
  <div class="house-photo" role="img" aria-label="Photo of a two-storey suburban house at dusk with a wet driveway and lawn"></div>
  <div class="brand-band">
    <div class="brand-name">THE OAKMERE REALTOR</div>
    <div class="brand-tag">You&nbsp; KNOW it won’t last long !</div>
  </div>
  <div class="front-headshot" role="img" aria-label="Agent headshot"></div>
</section>

<section class="card card-back" aria-label="Postcard back">
  <div class="intro">
    <div class="selling-bar">
      <span class="selling-title">SELLING</span>
      <span class="selling-sub">Choosing the right agent is<br>critical to your success</span>
    </div>
    <p class="intro-copy">Your home is your biggest asset.<br>You owe it to yourself to have every advantage by choosing the local agent with the expertise to position your Oakmere home and get it sold fast and for top dollar.<br>There is no other agent who knows the Oakmere market better.</p>
    <p class="intro-cta">Contact me today to get your home sold.</p>
  </div>
  <div class="contact-band">
    <div class="logo-block">
      <div class="logo-name">willowrun</div>
      <div class="logo-phone">(555) 310-4400</div>
    </div>
    <div class="badges"><span class="badge"></span><span class="badge"></span></div>
    <div class="reasons">
      <p>There are 3 key reasons a home doesn’t sell, and #1 is choosing the wrong agent to market your property.</p>
      <p>Contact me today to discuss yours home’s value and what steps I will take to assure your success</p>
    </div>
    <div class="divider"></div>
    <div class="back-headshot" role="img" aria-label="Agent headshot"></div>
    <div class="agent">
      <div class="agent-name">Marco Delvecchio</div>
      “The Oakmere Realtor”<br>
      Principal Broker, REALTOR<br>
      Willow Run Real Estate<br>
      O: (555) 310 4400<br>
      C: (555) 284 7192<br>
      www.oakmerehomes.com
    </div>
  </div>
</section>

</body>
</html>
```